Fahrzeugbeschriftung für Unternehmen im Bereich der Glasfaser-Montage
Zielgruppe
Wir sind im Bereich der Glasfaser-Montage tätig,
einblasen von Glasfaser Kabel, herstellen von LWL Splicen
Tätigkeitsstichworte:
LWL Einblasarbeiten
LWL Splicearbeiten
Entstörungsservice
Druckprüfunge Kavorinrohre
Aufgabenstellung
Die Beschriftung muss sich an der vorhandenen KFZ Beschriftung der Marq Elektro GmbH orientieren, da
wir uns mit dieser Firmen zusammen schließen werden.

```html
<!DOCTYPE html>
<html lang="de">
<head>
<meta charset="utf-8">
<title>Marq Elektro – Fahrzeugbeschriftung</title>
<link href="https://fonts.googleapis.com/css2?family=Roboto+Condensed:wght@400;700&display=swap" rel="stylesheet">
<style>
  :root {
    --brand-green: #139a74;
    --logo-green: #15b087;
    --band-grey: #b4b4b4;
    --panel-white: #f1f2f2;
    --window-dark: #161616;
    --ink: #1c1c1c;
    --page: #ffffff;
  }
  html, body {
    margin: 0;
    width: 1200px;
    height: 1044px;
    overflow: hidden;
    background: var(--page);
  }
  .wrap-layout { display: block; width: 1200px; height: 1044px; }
  .panel { fill: var(--panel-white); stroke: #d4d6d6; stroke-width: 1.5; }
  .window { fill: var(--window-dark); }
  .band { fill: var(--band-grey); }
  .stripe { fill: var(--brand-green); }
  .brand-name {
    font-family: "Roboto Condensed", sans-serif;
    font-weight: 700;
    fill: var(--brand-green);
  }
  .contact {
    font-family: "Roboto Condensed", sans-serif;
    font-weight: 400;
    fill: var(--ink);
  }
  .service-list {
    font-family: "Roboto Condensed", sans-serif;
    font-weight: 700;
    font-size: 15px;
    fill: var(--ink);
  }
  .bullet { fill: var(--brand-green); }
  .logo-lockup .brand-name { fill: var(--logo-green); }
  .logo-lockup .mark { fill: var(--logo-green); }
</style>
</head>
<body>
<svg class="wrap-layout" viewBox="0 0 1200 1044" xmlns="http://www.w3.org/2000/svg">
  <defs>
    <clipPath id="rear-clip"><rect x="30" y="100" width="330" height="540" rx="24"/></clipPath>
    <clipPath id="side-clip"><rect x="380" y="100" width="790" height="560" rx="24"/></clipPath>
    <linearGradient id="device-tones" x1="0" y1="0" x2="1" y2="1">
      <stop offset="0" stop-color="#2a2622"/>
      <stop offset=".45" stop-color="#a88a3e"/>
      <stop offset=".8" stop-color="#2b2550"/>
      <stop offset="1" stop-color="#3d3a7a"/>
    </linearGradient>
  </defs>

  <!-- Rear doors -->
  <g class="rear-doors" clip-path="url(#rear-clip)">
    <rect class="panel" x="30" y="100" width="330" height="540" rx="24"/>
    <rect class="window" x="48" y="190" width="296" height="230" rx="34"/>
    <polygon class="band" points="30,470 360,270 360,340 30,540"/>
    <polygon class="stripe" points="30,540 360,340 360,350 30,550"/>
    <text class="brand-name" font-size="54" transform="translate(60 435) rotate(-31)">Marq Elektro</text>
    <g class="contact" font-size="13" transform="translate(75 443) rotate(-31)">
      <text x="0" y="22">78000 Seestadt · Tel. 07700 - 4821</text>
      <text x="30" y="40">www.marq-elektro.de</text>
    </g>
    <g class="service-list">
      <rect class="bullet" x="197" y="500" width="5" height="7"/><text x="207" y="508">LWL Einblasarbeiten</text>
      <rect class="bullet" x="197" y="520" width="5" height="7"/><text x="207" y="528">LWL Splicearbeiten</text>
      <rect class="bullet" x="197" y="540" width="5" height="7"/><text x="207" y="548">Entstörungsservice</text>
      <rect class="bullet" x="197" y="560" width="5" height="7"/><text x="207" y="568">Druckprüfunge</text>
      <text x="207" y="588">Kavorinrohre</text>
    </g>
  </g>

  <!-- Side panel -->
  <g class="side-panel" clip-path="url(#side-clip)">
    <rect class="panel" x="380" y="100" width="790" height="560" rx="24"/>
    <polygon fill="url(#device-tones)" points="380,100 1000,100 380,570" role="img" aria-label="Nahaufnahme eines Glasfaser-Spleißgeräts"/>
    <rect class="window" x="815" y="260" width="170" height="150" rx="10"/>
    <rect class="window" x="1000" y="280" width="120" height="130" rx="12"/>
    <polygon class="band" points="380,640 1170,230 1170,300 380,710"/>
    <polygon class="stripe" points="380,710 1170,300 1170,312 380,722"/>
    <text class="brand-name" font-size="76" transform="translate(560 530) rotate(-27.4)">Marq Elektro</text>
    <text class="contact" font-size="17" transform="translate(600 526) rotate(-27.4)" y="38">78000 Seestadt · Tel. 07700 - 4821 · www.marq-elektro.de</text>
    <g class="service-list" font-size="16">
      <rect class="bullet" x="840" y="501" width="5" height="8"/><text x="850" y="510">LWL Einblasarbeiten</text>
      <rect class="bullet" x="840" y="523" width="5" height="8"/><text x="850" y="532">LWL Splicearbeiten</text>
      <rect class="bullet" x="840" y="545" width="5" height="8"/><text x="850" y="554">Entstörungsservice</text>
      <rect class="bullet" x="840" y="567" width="5" height="8"/><text x="850" y="576">Druckprüfunge Kavorinrohre</text>
    </g>
  </g>

  <!-- Standalone brand lockup -->
  <g class="logo-lockup">
    <rect class="mark" x="940" y="915" width="18" height="18"/>
    <text class="brand-name" x="966" y="933" font-size="34">Marq Elektro</text>
  </g>
</svg>
</body>
</html>
```